Education related business need name card design

We need name card design for long term study agent.
Company name is Harbor Lantern.
We support clients to connect to the world.
Clients are Japanese family who has primary and secondary school students.

Company Logo is reflection of the globe and HL (Harbor Lantern).
Since business is related to education, we would like to show reliability and love to see the world map (atlas) in the name card.

Target Market(s)

late 30's to 50's parents of primary and secondary students who are enthusiastic for education. Secondary school management

Industry/Entity Type

Education

Contact Information for Business Card

Company name, Address, Official position, Name, Phone number, Mobile number, email address,

Font styles to use
Serif
Other font styles liked:
• Century Gothic(logo)

Requirements
Must have
• Since businee is related to education, we would like to show reliability and love to see the world map (atlas) in the name card.

```html
<!DOCTYPE html>
<html lang="en">
<head>
<meta charset="utf-8">
<title>Harbor Lantern — Business Card</title>
<link rel="stylesheet" href="https://fonts.googleapis.com/css2?family=Questrial&display=swap">
<style>
  :root {
    --backdrop: #9a9a9a;
    --card-white: #f3f3f4;
    --brand-blue: #0a6bb0;
    --name-blue: #1a72b8;
    --company-navy: #1c4a8e;
    --text-grey: #555a60;
    --rule-blue: #2a7cc0;
    --white: #ffffff;
  }
  * { margin: 0; padding: 0; box-sizing: border-box; }
  html, body {
    width: 1105px;
    height: 1200px;
    overflow: hidden;
    background: var(--backdrop);
    font-family: "Questrial", "Century Gothic", sans-serif;
  }
  .canvas { position: relative; width: 1105px; height: 1200px; }
  .card {
    position: absolute;
    left: 182px;
    width: 747px;
    height: 425px;
  }
  .card--front { top: 119px; background: var(--card-white); }
  .card--back { top: 637px; background: var(--brand-blue); }

  /* Front: brand block */
  .brand {
    position: absolute;
    left: 38px;
    top: 92px;
    width: 320px;
    text-align: center;
  }
  .brand__mark {
    display: block;
    width: 112px;
    height: 112px;
    margin: 0 auto 42px;
    border-radius: 50%;
    background: var(--brand-blue);
  }
  .brand__name {
    color: var(--company-navy);
    font-size: 21px;
    letter-spacing: -0.2px;
    white-space: nowrap;
  }

  /* Front: details */
  .details {
    position: absolute;
    left: 388px;
    top: 68px;
    width: 300px;
  }
  .details__name {
    color: var(--name-blue);
    font-size: 29px;
    font-weight: 400;
    letter-spacing: 0.3px;
    -webkit-text-stroke: 0.6px var(--name-blue);
    line-height: 1.1;
  }
  .details__title {
    color: var(--name-blue);
    font-size: 21px;
    margin-top: 2px;
  }
  .details__rule {
    height: 2px;
    background: var(--rule-blue);
    width: 277px;
  }
  .details__rule--top { margin-top: 12px; }
  .details__address {
    color: var(--text-grey);
    font-size: 21px;
    line-height: 28px;
    margin: 10px 0 8px;
    font-style: normal;
  }
  .contact-list { list-style: none; margin-top: 10px; }
  .contact-list li {
    display: flex;
    align-items: center;
    color: var(--text-grey);
    font-size: 21px;
    height: 29px;
  }
  .contact-list svg {
    width: 17px;
    height: 17px;
    margin-right: 12px;
    flex: none;
    fill: var(--name-blue);
  }

  /* Back */
  .back-brand {
    position: absolute;
    left: 0;
    right: 0;
    top: 88px;
    text-align: center;
    color: var(--white);
  }
  .back-brand__mark {
    display: block;
    width: 150px;
    height: 150px;
    margin: 0 auto 20px;
    border-radius: 50%;
    background: var(--white);
  }
  .back-brand__name { font-size: 26px; letter-spacing: 1px; }
  .back-web {
    position: absolute;
    left: 0;
    right: 0;
    top: 358px;
    text-align: center;
    color: var(--white);
    font-size: 21px;
    letter-spacing: 4px;
  }
</style>
</head>
<body>
<main class="canvas">

  <section class="card card--front" aria-label="Card front">
    <div class="brand">
      <span class="brand__mark" aria-hidden="true"></span>
      <p class="brand__name">Harbor Lantern Pte.Ltd.</p>
    </div>

    <div class="details">
      <h1 class="details__name">Kenji Morrow</h1>
      <p class="details__title">CEO/Founder</p>
      <div class="details__rule details__rule--top"></div>
      <address class="details__address">2140 Tidewater Road<br>Portland, Maine 04101</address>
      <div class="details__rule"></div>
      <ul class="contact-list">
        <li>
          <svg viewBox="0 0 24 24" aria-hidden="true"><path d="M6.6 10.8a15.1 15.1 0 0 0 6.6 6.6l2.2-2.2c.3-.3.7-.4 1-.2 1.1.4 2.3.6 3.6.6.6 0 1 .4 1 1V20c0 .6-.4 1-1 1A17 17 0 0 1 3 4c0-.6.4-1 1-1h3.5c.6 0 1 .4 1 1 0 1.3.2 2.5.6 3.6.1.3 0 .7-.2 1z"/></svg>
          207 555 0148
        </li>
        <li>
          <svg viewBox="0 0 24 24" aria-hidden="true"><path d="M7 1h10a2 2 0 0 1 2 2v18a2 2 0 0 1-2 2H7a2 2 0 0 1-2-2V3a2 2 0 0 1 2-2zm0 3v14h10V4zm5 15.5a1.2 1.2 0 1 0 0 2.4 1.2 1.2 0 0 0 0-2.4z"/></svg>
          207 555 0193
        </li>
        <li>
          <svg viewBox="0 0 24 24" aria-hidden="true"><path d="M2 5h20v14H2zm2 2v.5l8 5 8-5V7zm0 2.8V17h16V9.8l-8 5z"/></svg>
          kenji@harborlantern.com
        </li>
        <li>
          <svg viewBox="0 0 24 24" aria-hidden="true"><path d="M12 2a10 10 0 1 0 0 20 10 10 0 0 0 0-20zm-1 17.9A8 8 0 0 1 4.1 10L9 15v1a2 2 0 0 0 2 2zm6.9-2.5A2 2 0 0 0 16 16h-1v-3a1 1 0 0 0-1-1H8v-2h2a1 1 0 0 0 1-1V7h2a2 2 0 0 0 2-2v-.4a8 8 0 0 1 2.9 12.8z"/></svg>
          www.harborlantern.com
        </li>
      </ul>
    </div>
  </section>

  <section class="card card--back" aria-label="Card back">
    <div class="back-brand">
      <span class="back-brand__mark" aria-hidden="true"></span>
      <p class="back-brand__name">Harbor Lantern</p>
    </div>
    <p class="back-web">www.harborlantern.com</p>
  </section>

</main>
</body>
</html>
```